Simple proffessional BC

I have a logo which I will attach below.
I would like the logo on the front of the card with these details in point form below:
Pre and Post Natal Yoga: Pregnancy Workshops: Hypnobirthing Courses
On the back of the card my details:
Merrin Galvey
Facebook page- calmbellieswillowharbour
Mobile- 0438 512 740

I like the idea of the card being simple, possibly just the above on a plain coloured (eggshell?) card, a card that is textured.
I am open to suggestion if it appeals!
Thank you and good luck!

Target Market(s)

Pregnant women, 20's-40's

Requirements
Must have
• Simple, compliment logo.
Make logo the feature.
Should not have

• .

```html
<!DOCTYPE html>
<html lang="en">
<head>
<meta charset="utf-8">
<title>Calm Bellies – Business Card</title>
<link rel="stylesheet" href="https://fonts.googleapis.com/css2?family=Dancing+Script:wght@500;700&display=swap">
<style>
  :root {
    --backdrop: #ece8e1;
    --card-cream: #f4eec6;
    --card-cream-deep: #ece2b0;
    --mark-faint: #f0d9a0;
    --brand-orange: #eea53a;
    --brand-red: #8c1a1a;
    --ink: #1c1712;
    --shadow: rgba(40, 30, 20, 0.22);
  }
  * { margin: 0; padding: 0; box-sizing: border-box; }
  html, body {
    width: 1200px;
    height: 900px;
    overflow: hidden;
    background: var(--backdrop);
  }
  .canvas {
    width: 1200px;
    height: 900px;
    display: flex;
    align-items: center;
    justify-content: center;
    gap: 60px;
  }
  .card {
    position: relative;
    width: 510px;
    height: 330px;
    overflow: hidden;
    background: radial-gradient(ellipse at 40% 35%, var(--card-cream) 0%, var(--card-cream) 55%, var(--card-cream-deep) 100%);
    box-shadow: 0 10px 28px var(--shadow);
    font-family: "Dancing Script", cursive;
  }

  /* Back: contact details */
  .card-back .watermark-circle {
    position: absolute;
    left: 195px;
    top: 34px;
    width: 150px;
    height: 150px;
    border-radius: 50%;
    background: var(--mark-faint);
    opacity: 0.75;
  }
  .card-back .contact {
    position: absolute;
    left: 26px;
    bottom: 30px;
    color: var(--ink);
    font-weight: 700;
    font-size: 25px;
    line-height: 1.2;
  }

  /* Front: brand and services */
  .card-front .brand {
    position: absolute;
    right: 70px;
    top: 72px;
    display: flex;
    align-items: center;
    gap: 10px;
  }
  .card-front .brand-dot {
    width: 38px;
    height: 38px;
    border-radius: 50%;
    background: var(--brand-orange);
  }
  .card-front .brand-name {
    color: var(--brand-red);
    font-weight: 500;
    font-size: 36px;
  }
  .card-front .band {
    position: absolute;
    left: 0;
    right: 0;
    top: 176px;
    height: 16px;
    background: var(--brand-red);
  }
  .card-front .services {
    position: absolute;
    left: 0;
    right: 0;
    top: 192px;
    bottom: 0;
    background: var(--brand-orange);
    list-style: none;
    padding: 28px 0 0 36px;
    color: var(--brand-red);
    font-weight: 700;
    font-size: 25px;
    line-height: 1.25;
  }
</style>
</head>
<body>
  <main class="canvas">
    <section class="card card-back" aria-label="Card back">
      <div class="watermark-circle" aria-hidden="true"></div>
      <div class="contact">
        <p class="contact-name">Merrin Galvey</p>
        <p class="contact-social">Fb: calmbellieswillowharbour</p>
        <p class="contact-phone">0438 512 740</p>
      </div>
    </section>

    <section class="card card-front" aria-label="Card front">
      <div class="brand">
        <span class="brand-dot" aria-hidden="true"></span>
        <span class="brand-name">Calm Bellies</span>
      </div>
      <div class="band" aria-hidden="true"></div>
      <ul class="services">
        <li>Pre and Post Natal Yoga</li>
        <li>Pregnancy Workshops</li>
        <li>Hypnobirthing Courses</li>
      </ul>
    </section>
  </main>
</body>
</html>
```